Romantic Experiences Business Needs Banner Ad Design Project

We are going to run a branding campaign and we need banner ad design for a company based in Mexico City called "CARENSOLTA".

We create romantic experiences or moments for couples celebrating special dates, for instance birthdays, wedding anniversaries and original ways to give an engagement ring. These experiences may have components like romantic dinner, chamber musicians, astronomer, concierges, fireworks, mansions, romantic tours on helicopter and yacht.

The final design should communicate our main task "romantic moment design" and brand attributes: sophisticated, elegant and romantic.

You can visit the webpage at: http://www.carensolta.com.mx

Target Market(s)

People from 25 to 50 years old who wants to celebrate wedding anniversary or give an engagement ring

Industry/Entity Type

Wedding

Requirements
Must have
• - Logo
- Banner sizes: 300x250, 728x90,160x600
Nice to have
• - Call to Action
- Theme: "Diseño Momentos Románticos"

```html
<!DOCTYPE html>
<html lang="es">
<head>
<meta charset="utf-8">
<title>CARENSOLTA — Banner Set</title>
<link rel="stylesheet" href="https://fonts.googleapis.com/css2?family=Open+Sans:wght@400;600;700&display=swap">
<style>
  :root {
    --stage: #f1f1f1;
    --banner-bg: #000000;
    --ink-light: #ffffff;
    --photo-deep: #5a1f3a;
    --photo-mid: #b44a73;
    --photo-warm: #e07a9a;
    --button-top: #4fb2d6;
    --button-bottom: #0b5f86;
    --button-edge: #0a4a6a;
  }
  * { margin: 0; padding: 0; box-sizing: border-box; }
  html, body { width: 1200px; height: 1000px; overflow: hidden; }
  body {
    position: relative;
    background: radial-gradient(ellipse at center, #ffffff 0%, var(--stage) 60%, #e2e2e2 100%);
    font-family: "Open Sans", sans-serif;
  }
  .banner {
    position: absolute;
    background: var(--banner-bg);
    color: var(--ink-light);
    overflow: hidden;
    box-shadow: 0 0 40px rgba(0,0,0,0.35);
  }
  .photo {
    position: absolute;
    background:
      radial-gradient(ellipse at 25% 50%, rgba(255,190,210,0.5), transparent 55%),
      radial-gradient(ellipse at 75% 40%, rgba(255,160,190,0.45), transparent 50%),
      linear-gradient(90deg, var(--photo-deep), var(--photo-mid) 45%, var(--photo-warm) 60%, var(--photo-deep));
  }
  .brand-name {
    position: absolute;
    left: 0; right: 0;
    text-align: center;
    font-family: "Open Sans", sans-serif;
    font-weight: 400;
    line-height: 1;
    white-space: nowrap;
  }
  .tagline {
    position: absolute;
    left: 0; right: 0;
    text-align: center;
    font-size: 7.5px;
    font-weight: 400;
    letter-spacing: 3.2px;
    line-height: 1;
    white-space: nowrap;
  }
  .cta {
    position: absolute;
    display: flex;
    align-items: center;
    justify-content: center;
    color: var(--ink-light);
    text-decoration: none;
    font-weight: 600;
    border-radius: 4px;
    border: 1px solid var(--button-edge);
    background: linear-gradient(180deg, var(--button-top) 0%, #1d86b2 48%, var(--button-bottom) 52%, #0d6f98 100%);
    box-shadow: inset 0 1px 0 rgba(255,255,255,0.5);
  }

  /* 728 x 90 leaderboard */
  .leaderboard { left: 246px; top: 80px; width: 728px; height: 90px; }
  .leaderboard .brand-panel { position: absolute; left: 0; top: 0; width: 307px; height: 90px; }
  .leaderboard .brand-name { top: 9px; font-size: 30px; letter-spacing: 3px; }
  .leaderboard .tagline { top: 42px; }
  .leaderboard .cta { left: 94px; top: 58px; width: 108px; height: 22px; font-size: 12.5px; }
  .leaderboard .photo { left: 307px; top: 0; width: 421px; height: 90px; }

  /* 300 x 250 rectangle */
  .rectangle { left: 246px; top: 652px; width: 300px; height: 250px; }
  .rectangle .photo { left: 0; top: 0; width: 300px; height: 151px; }
  .rectangle .brand-name { top: 164px; font-size: 30px; letter-spacing: 3px; }
  .rectangle .tagline { top: 198px; }
  .rectangle .cta { left: 87px; top: 215px; width: 124px; height: 25px; font-size: 14px; }

  /* 160 x 600 skyscraper */
  .skyscraper { left: 814px; top: 302px; width: 160px; height: 600px; }
  .skyscraper .brand-name { top: 67px; font-size: 17px; letter-spacing: 1.2px; }
  .skyscraper .cta { left: 25px; top: 106px; width: 108px; height: 22px; font-size: 12.5px; }
  .skyscraper .diagonal { position: absolute; left: 0; top: 0; }
  .skyscraper .diagonal text {
    font-family: "Open Sans", sans-serif;
    font-size: 11px;
    font-weight: 600;
    fill: var(--ink-light);
  }
  .skyscraper .diagonal .line-top { letter-spacing: 7px; }
  .skyscraper .diagonal .line-bottom { letter-spacing: 9.5px; }
</style>
</head>
<body>

  <section class="banner leaderboard" aria-label="Banner 728x90">
    <div class="brand-panel">
      <h1 class="brand-name">CARENSOLTA</h1>
      <p class="tagline">EXPERIENCIAS ROMÁNTICAS</p>
      <a class="cta" href="http://www.carensolta.com.mx">Learn More</a>
    </div>
    <div class="photo" role="img" aria-label="Photo of a couple toasting with red wine at a romantic dinner"></div>
  </section>

  <section class="banner skyscraper" aria-label="Banner 160x600">
    <h2 class="brand-name">CARENSOLTA</h2>
    <a class="cta" href="http://www.carensolta.com.mx">Learn More</a>
    <svg class="diagonal" width="160" height="600" viewBox="0 0 160 600">
      <defs>
        <linearGradient id="photo-tone" x1="0" y1="0" x2="1" y2="1">
          <stop offset="0" stop-color="#5a1f3a"/>
          <stop offset="0.45" stop-color="#b44a73"/>
          <stop offset="0.7" stop-color="#e07a9a"/>
          <stop offset="1" stop-color="#4a1a30"/>
        </linearGradient>
      </defs>
      <polygon points="0,204 160,284 160,518 0,438" fill="url(#photo-tone)" role="img" aria-label="Photo of a couple toasting with red wine at a romantic dinner"/>
      <text class="line-top" transform="translate(6,194) rotate(28)">EXPERIENCIAS</text>
      <text class="line-bottom" transform="translate(6,460) rotate(28)">ROMÁNTICAS</text>
    </svg>
  </section>

  <section class="banner rectangle" aria-label="Banner 300x250">
    <div class="photo" role="img" aria-label="Photo of a couple toasting with red wine at a romantic dinner"></div>
    <h2 class="brand-name">CARENSOLTA</h2>
    <p class="tagline">EXPERIENCIAS ROMÁNTICAS</p>
    <a class="cta" href="http://www.carensolta.com.mx">Learn More</a>
  </section>

</body>
</html>
```